Banner ad Design

Project:
Creation of online advertising banners for use on Brixel AdPlume network and for display advertising on one product on our website.
http://brightparcel.com.au/computers/ebook/7inch-velmora-3g-mini-tablet-netbook-colour-ebook-reader.html
Headline to appear on all banners:
Hot!!! 3G Velmora tablet Only $159 (with our website logo )
Formats
- 728 x 90
- 468 x 60
- 300 x 250
- 160 x 600
- 120 x 600
- 336 x 280
Note: Would prefer to have banners ASAP (sooner than 5 days if possible). Designers who act on it quickly, and supply great designs will most likely be awarded the winner
Advertising

```html
<!DOCTYPE html>
<html lang="en">
<head>
<meta charset="utf-8">
<title>BrightParcel – Hot!!! 3G Velmora Tablet Banners</title>
<link rel="stylesheet" href="https://fonts.googleapis.com/css2?family=Anton&family=Oswald:wght@700&display=swap">
<style>
  :root {
    --canvas: #000000;
    --cream: #fffdf3;
    --ray: #fde9b8;
    --sun: #ffd23a;
    --flame: #f39a1d;
    --flame-deep: #e1561a;
    --hot-red: #e5261c;
    --brand-green: #1f7a3a;
    --only-yellow: #e9e21a;
    --ink: #1a1a1a;
    --white: #ffffff;
    --device: #3a3d44;
    --screen: #d9dde3;
    --photo-warm: #b98563;
    --photo-dark: #3a2a22;
  }
  * { box-sizing: border-box; margin: 0; padding: 0; }
  html, body { width: 1200px; height: 900px; overflow: hidden; background: var(--canvas); }
  .canvas { position: relative; width: 1200px; height: 900px; }

  .banner { position: absolute; overflow: hidden; }
  .banner--leaderboard { left: 194px; top: 26px; width: 846px; height: 104px;
    background: linear-gradient(90deg, var(--cream) 0%, var(--cream) 70%, var(--ray) 100%); }
  .banner--skyscraper { left: 194px; top: 158px; width: 188px; height: 698px;
    background: linear-gradient(180deg, var(--cream) 0%, var(--cream) 40%, var(--ray) 55%, var(--sun) 78%, var(--flame) 100%); }
  .banner--rectangle { left: 408px; top: 158px; width: 390px; height: 326px;
    background: radial-gradient(circle at 20% 20%, var(--cream) 0%, var(--cream) 30%, var(--ray) 60%, var(--sun) 100%); }

  .flames { position: absolute; background: linear-gradient(180deg, rgba(243,154,29,0) 0%, var(--flame) 55%, var(--flame-deep) 100%); }

  .logo { position: absolute; display: flex; align-items: center; gap: 4px;
    font-family: "Oswald", sans-serif; font-weight: 700; color: var(--brand-green); white-space: nowrap; line-height: 1; }
  .logo__mark { background: var(--flame); border-radius: 2px; }

  .tablet-shot { position: absolute; border-radius: 6px;
    background: linear-gradient(160deg, var(--device) 0%, var(--device) 12%, var(--screen) 13%, var(--white) 60%, var(--screen) 87%, var(--device) 88%); }

  .photo { position: absolute;
    background: linear-gradient(180deg, var(--photo-warm) 0%, #a9775a 55%, var(--photo-dark) 100%); }

  .hot { position: absolute; font-family: "Anton", sans-serif; color: var(--hot-red); line-height: 1;
    text-shadow: -2px -2px 0 var(--white), 2px -2px 0 var(--white), -2px 2px 0 var(--white), 2px 2px 0 var(--white), 3px 4px 0 rgba(0,0,0,.25); }
  .product { position: absolute; font-family: "Oswald", sans-serif; font-weight: 700; color: var(--brand-green); line-height: 1; text-align: center; }
  .product__line { display: block; }
  .price { position: absolute; font-family: "Anton", sans-serif; line-height: 1; }
  .price__only { display: inline-block; font-family: "Oswald", sans-serif; font-weight: 700; color: var(--ink);
    background: var(--only-yellow); padding: 0 4px; transform: rotate(-8deg); }
  .price__amount { display: block; color: var(--white);
    text-shadow: -2px -2px 0 var(--ink), 2px -2px 0 var(--ink), -2px 2px 0 var(--ink), 2px 2px 0 var(--ink), 0 3px 0 var(--ink); }
</style>
</head>
<body>
<main class="canvas">

  <!-- 728 x 90 leaderboard -->
  <section class="banner banner--leaderboard" aria-label="Leaderboard banner">
    <div class="flames" style="left:600px; top:40px; width:246px; height:64px;" role="img" aria-label="Flame illustration"></div>
    <div class="logo" style="left:14px; top:42px; font-size:20px;"><span>BrightParcel</span><span class="logo__mark" style="width:14px;height:16px;"></span></div>
    <div class="tablet-shot" style="left:168px; top:-10px; width:78px; height:116px; transform:rotate(6deg);" role="img" aria-label="3G Velmora tablet"></div>
    <div class="hot" style="left:258px; top:18px; font-size:58px; background:var(--white); padding:4px 6px;">HOT!!!</div>
    <div class="product" style="left:404px; top:14px; width:150px;">
      <span class="product__line" style="font-size:26px;">3G Velmora</span>
      <span class="product__line" style="font-size:42px;">Tablet</span>
    </div>
    <div class="price" style="left:566px; top:16px;">
      <span class="price__only" style="font-size:16px;">Only</span>
      <span class="price__amount" style="font-size:50px; margin-top:-10px;">$159</span>
    </div>
    <div class="photo" style="left:734px; top:0; width:112px; height:104px;" role="img" aria-label="Photo of a surprised young man"></div>
  </section>

  <!-- 160 x 600 skyscraper -->
  <section class="banner banner--skyscraper" aria-label="Skyscraper banner">
    <div class="flames" style="left:0; top:520px; width:188px; height:178px;" role="img" aria-label="Flame illustration"></div>
    <div class="logo" style="left:36px; top:20px; font-size:24px;"><span>BrightParcel</span><span class="logo__mark" style="width:16px;height:20px;"></span></div>
    <div class="tablet-shot" style="left:14px; top:56px; width:120px; height:150px; transform:rotate(8deg);" role="img" aria-label="3G Velmora tablet"></div>
    <div class="hot" style="left:6px; top:176px; font-size:68px; transform:rotate(-4deg);">HOT!!!</div>
    <div class="product" style="left:0; top:268px; width:188px;">
      <span class="product__line" style="font-size:28px;">3G Velmora</span>
      <span class="product__line" style="font-size:44px;">Tablet</span>
    </div>
    <div class="price" style="left:30px; top:358px;">
      <span class="price__only" style="font-size:18px;">Only</span>
      <span class="price__amount" style="font-size:64px; margin-top:-10px;">$159</span>
    </div>
    <div class="photo" style="left:24px; top:500px; width:150px; height:198px;" role="img" aria-label="Photo of a surprised young man"></div>
  </section>

  <!-- 300 x 250 rectangle -->
  <section class="banner banner--rectangle" aria-label="Medium rectangle banner">
    <div class="flames" style="left:0; top:196px; width:390px; height:130px;" role="img" aria-label="Flame illustration"></div>
    <div class="logo" style="left:206px; top:24px; font-size:28px;"><span>BrightParcel</span><span class="logo__mark" style="width:18px;height:22px;"></span></div>
    <div class="tablet-shot" style="left:50px; top:-16px; width:76px; height:118px; transform:rotate(10deg);" role="img" aria-label="3G Velmora tablet"></div>
    <div class="hot" style="left:16px; top:88px; font-size:56px; transform:rotate(-6deg);">HOT!!!</div>
    <div class="product" style="left:8px; top:156px; width:150px;">
      <span class="product__line" style="font-size:26px;">3G Velmora</span>
      <span class="product__line" style="font-size:40px;">Tablet</span>
    </div>
    <div class="price" style="left:30px; top:230px;">
      <span class="price__only" style="font-size:15px;">Only</span>
      <span class="price__amount" style="font-size:46px; margin-top:-8px;">$159</span>
    </div>
    <div class="photo" style="left:166px; top:112px; width:224px; height:214px;" role="img" aria-label="Photo of a surprised young man"></div>
  </section>

</main>
</body>
</html>
```